New Postcard Design Project for home loan

The project is for home loan for business owners that do no need to have any income statements. NO W2, NO TAX RETURNS, NO PAYSTUBS , CALL /TEXT/EMAIL DELVIN OKAFOR DOKAFOR@VELTORHOMEFUND.COM 555.294.8163

GET LICENSE INFORMATION FROM WEBSITE:

Here is the information you will need to have on the mailer:

- LO Name
- LO NMLS
- Branch Name (if applicable)
- Branch NMLS (if applicable)
- Branch Address (if applicable)
- Veltor Corporation
- Veltor NMLS
- Veltor Address
- Veltor Phone Number

And since you’re going to be talking about rates, you will need the following information as well:
1. Amount of the represented loan.
2. Repayment term in years of the represented loan.
3. Prepayment terms.
4. If the advertised rate may increase, the ad must state: "Advertised rate may increase"
5. Statement: "Restrictions may apply. Programs not available in all areas."

Target Market(s)

home owners that own a business

Industry/Entity Type

Home Loan refinance

Font styles to use
Serif

Colors
59FF00
82FF00
B8FF75
E3FFCB
F4FFEA
F0912C
F2A743
F7CA91
FBE8D2
FDF5EE
EE7325
F08F49
F5BC92
FAE3D3
FDF4ED
EB3D1F
EC4F4E
F09395
F8D3D4
FCEDEE

Requirements
Must have
• Must have No W2, No Tax Returns, No Paystubs Required. Must have picture of home. Home loans for business owners without traditional tax returns. MUST HAVE LOAN DISCLOSURES.
Nice to have
• Pictures of Home loan Make the customer Call the loan officer. 555.294.8163
Should not have
• My website you can extract logo: https://www.veltorhomefund.com/delvinokafor

```html
<!DOCTYPE html>
<html lang="en">
<head>
<meta charset="utf-8">
<title>Veltor Home Fund – Dream Home Postcard</title>
<link rel="stylesheet" href="https://fonts.googleapis.com/css2?family=Montserrat:wght@400;500;700;800;900&family=Arimo:wght@400;700&display=swap">
<style>
  :root{
    --blue:#2f86c6;
    --blue-deep:#1d6499;
    --navy:#0d3d5f;
    --ink:#1f1f1f;
    --charcoal:#262626;
    --grey-text:#4a4a4a;
    --placeholder:#d9d9d9;
    --paper:#ffffff;
    --page:#ffffff;
    --rule:#5c5c5c;
  }
  *{box-sizing:border-box;margin:0;padding:0}
  html,body{width:800px;height:1200px;overflow:hidden;background:var(--page)}
  body{font-family:"Arimo",Arial,sans-serif;color:var(--ink);position:relative}
  .postcard{position:absolute;left:44px;width:711px;height:508px;background:var(--paper);overflow:hidden;box-shadow:0 2px 8px rgba(0,0,0,.18)}
  .postcard--front{top:60px}
  .postcard--back{top:632px}
  .abs{position:absolute}

  /* FRONT */
  .brand{font-family:"Montserrat",sans-serif;font-weight:700;color:var(--blue);font-size:36px;letter-spacing:-.5px;left:20px;top:18px;display:flex;align-items:center;gap:8px}
  .brand__mark{width:12px;height:12px;background:var(--blue)}
  .headline-pre{left:18px;top:88px;font-family:"Montserrat",sans-serif;font-weight:500;font-size:25px;letter-spacing:1.5px;color:var(--ink)}
  .headline{left:15px;top:112px;font-family:"Montserrat",sans-serif;font-weight:900;font-size:66px;line-height:54px;color:var(--blue);letter-spacing:-1px}
  .headline-rule{left:15px;top:234px;width:262px;height:3px;background:var(--ink)}
  .subhead{left:15px;top:244px;font-family:"Montserrat",sans-serif;font-size:15.5px;line-height:17px;color:var(--ink)}
  .perks-band{left:0;top:288px;width:360px;height:28px;background:var(--navy);color:#fff;font-family:"Montserrat",sans-serif;font-weight:600;font-size:13px;display:flex;align-items:center;padding-left:15px;gap:10px}
  .perks-band .sep{opacity:.85}
  .resources{left:12px;top:328px;display:flex}
  .resource{width:88px;display:flex;flex-direction:column;align-items:center;text-align:center;font-family:"Montserrat",sans-serif;font-weight:600;font-size:10.5px;line-height:12px;color:var(--grey-text)}
  .resource__icon{width:34px;height:34px;background:var(--navy);margin-bottom:8px;display:flex;align-items:center;justify-content:center}
  .contact-band{left:0;top:418px;width:711px;height:90px;background:var(--charcoal)}
  .lo-photo{background:var(--placeholder)}
  .front-lo-photo{left:18px;top:406px;width:67px;height:78px}
  .offered-tag{left:96px;top:425px;background:var(--blue);color:#fff;font-family:"Montserrat",sans-serif;font-size:8px;font-weight:600;padding:1px 10px 1px 4px;clip-path:polygon(0 0,100% 0,88% 100%,0 100%)}
  .front-lo-name{left:96px;top:438px;color:#fff;font-family:"Montserrat",sans-serif;font-weight:800;font-size:16px}
  .front-lo-mail{left:96px;top:458px;color:#fff;font-family:"Montserrat",sans-serif;font-size:11.5px;display:flex;align-items:center;gap:4px}
  .divider{left:270px;top:424px;width:1px;height:62px;background:#8a8a8a}
  .front-contact{left:280px;top:422px;color:#fff;font-family:"Montserrat",sans-serif}
  .front-contact .row{display:flex;align-items:flex-start;gap:8px;margin-bottom:4px}
  .front-contact .phone{font-weight:700;font-size:12.5px}
  .front-contact .mail{font-size:10px}
  .front-contact .addr{font-size:8px;line-height:10px}
  .hero-photo{left:0;top:0}

  /* BACK */
  .about-panel{left:0;top:0;width:300px;height:198px;background:linear-gradient(180deg,var(--blue-deep),#2a7cb7)}
  .about-title{left:22px;top:18px;color:#fff;font-family:"Montserrat",sans-serif;font-weight:800;font-size:15px}
  .about-copy{left:22px;top:43px;width:195px;color:#fff;font-size:9.4px;line-height:11.9px}
  .rates-panel{left:0;top:198px;width:300px;height:77px;background:#2d2d2d}
  .rates-copy{left:22px;top:205px;font-family:"Montserrat",sans-serif;font-weight:700;font-size:13.5px;line-height:16.5px;color:#fff}
  .rates-copy .accent{color:#3b9ae0}
  .disclosures{left:22px;top:292px;list-style:none;font-size:9.4px;line-height:11.5px;color:var(--ink)}
  .disclosures li{display:flex;gap:8px;margin-bottom:8px}
  .disclosures svg{flex:none;margin-top:1px}
  .back-band{left:0;top:0}
  .back-lo-photo{left:20px;top:424px;width:52px;height:62px}
  .back-lo-name{left:83px;top:440px;color:#fff;font-family:"Montserrat",sans-serif;font-weight:700;font-size:14.5px}
  .back-lo-role{left:83px;top:456px;color:#fff;font-family:"Montserrat",sans-serif;font-size:11px}
  .back-lo-mail{left:83px;top:473px;color:#fff;font-size:8.5px;display:flex;gap:6px;align-items:center}
  .back-phone{left:226px;top:440px;color:#fff;font-family:"Montserrat",sans-serif;font-weight:700;font-size:16.5px;display:flex;gap:8px;align-items:center}
  .back-addr{left:226px;top:466px;color:#fff;font-size:7.6px;line-height:9.5px;display:flex;gap:8px}
  .stamp{left:582px;top:40px;width:88px;height:102px;background:var(--placeholder)}
  .address-line{left:431px;width:242px;height:1px;background:var(--rule)}
  .back-brand{left:592px;top:440px;font-family:"Montserrat",sans-serif;font-weight:700;font-size:21px;color:var(--blue);display:flex;align-items:center;gap:5px}
  .back-brand .brand__mark{width:7px;height:7px}
  .back-url{left:561px;top:467px;font-size:8.5px;color:var(--grey-text)}
</style>
</head>
<body>

<!-- FRONT -->
<section class="postcard postcard--front" aria-label="Postcard front">
  <div class="abs contact-band"></div>

  <svg class="abs hero-photo" width="711" height="508" viewBox="0 0 711 508">
    <defs>
      <linearGradient id="heroTones" x1="0" y1="0" x2="0" y2="1">
        <stop offset="0" stop-color="#9cc4e8"/>
        <stop offset=".3" stop-color="#d6e4ef"/>
        <stop offset=".45" stop-color="#76879a"/>
        <stop offset=".7" stop-color="#9ea7b0"/>
        <stop offset=".82" stop-color="#6f9a3c"/>
        <stop offset="1" stop-color="#4f8a27"/>
      </linearGradient>
    </defs>
    <ellipse cx="777" cy="200" rx="450" ry="380" fill="var(--navy)"/>
    <ellipse cx="789" cy="194" rx="444" ry="372" fill="url(#heroTones)" role="img" aria-label="Photo of a grey two-storey family home with white garage door and green lawn"/>
  </svg>

  <div class="abs brand">veltor<span class="brand__mark"></span></div>
  <div class="abs headline-pre">LOOKING FOR A</div>
  <div class="abs headline">DREAM<br>HOME?</div>
  <div class="abs headline-rule"></div>
  <div class="abs subhead">Home Loans for Business Owners<br>&nbsp;Without Traditional Tax Returns</div>

  <div class="abs perks-band">
    <span>NO W2</span><span class="sep">|</span><span>NO TAX RETURNS</span><span class="sep">|</span><span>NO PAYSTUBS</span>
  </div>

  <div class="abs resources">
    <div class="resource">
      <div class="resource__icon">
        <svg width="22" height="20" viewBox="0 0 22 20" fill="none" stroke="#fff" stroke-width="2"><path d="M2 10 L11 2 L20 10"/><path d="M5 8 V18 H17 V8"/><circle cx="11" cy="12" r="2" fill="#fff" stroke="none"/></svg>
      </div>Home<br>Buyer's Guide
    </div>
    <div class="resource">
      <div class="resource__icon">
        <svg width="20" height="20" viewBox="0 0 20 20" fill="none" stroke="#fff" stroke-width="1.8"><rect x="1" y="1" width="8" height="8"/><rect x="11" y="1" width="8" height="8"/><rect x="1" y="11" width="8" height="8"/><rect x="11" y="11" width="8" height="8"/></svg>
      </div>Refinance<br>Guide
    </div>
    <div class="resource">
      <div class="resource__icon">
        <svg width="18" height="22" viewBox="0 0 18 22" fill="none" stroke="#fff" stroke-width="1.8"><rect x="1" y="1" width="14" height="18"/><path d="M4 6 H12 M4 10 H12 M4 14 H12"/></svg>
      </div>Mortgage<br>Blog
    </div>
    <div class="resource">
      <div class="resource__icon">
        <svg width="16" height="22" viewBox="0 0 16 22" fill="none" stroke="#fff" stroke-width="1.8"><rect x="1" y="1" width="14" height="20"/><rect x="4" y="4" width="8" height="4"/><path d="M4 12 H6 M8 12 H10 M12 12 H12 M4 16 H6 M8 16 H10 M11 16 H12"/></svg>
      </div>Mortgage<br>Calculators
    </div>
  </div>

  <div class="abs lo-photo front-lo-photo" role="img" aria-label="Loan officer portrait"></div>
  <div class="abs offered-tag">OFFERED BY</div>
  <div class="abs front-lo-name">DELVIN OKAFOR</div>
  <div class="abs front-lo-mail">
    <svg width="10" height="8" viewBox="0 0 10 8" fill="none" stroke="#5aa6dd" stroke-width="1"><rect x=".5" y=".5" width="9" height="7"/><path d="M.5 .5 L5 4.5 L9.5 .5"/></svg>
    dokafor@veltorhomefund.com
  </div>
  <div class="abs divider"></div>
  <div class="abs front-contact">
    <div class="row"><svg width="12" height="11" viewBox="0 0 12 11" fill="#5aa6dd"><path d="M1 3 Q6 -1 11 3 L9 5 L8 3 H4 L3 5 Z M3 6 H9 L10 10 H2 Z"/></svg><span class="phone">555.294.8163</span></div>
    <div class="row"><svg width="12" height="10" viewBox="0 0 12 10" fill="none" stroke="#5aa6dd" stroke-width="1.2"><rect x=".6" y=".6" width="10.8" height="8.8"/><path d="M.6 .6 L6 5 L11.4 .6"/></svg><span class="mail">info@veltorhomefund.com</span></div>
    <div class="row"><svg width="12" height="13" viewBox="0 0 12 13" fill="#5aa6dd"><path d="M6 0 A5 5 0 0 1 11 5 C11 8 6 13 6 13 C6 13 1 8 1 5 A5 5 0 0 1 6 0 Z"/><circle cx="6" cy="5" r="2" fill="#262626"/></svg><span class="addr">48 Harlow Commerce Drive Suite 210<br>Brenford, PA 19077</span></div>
  </div>
</section>

<!-- BACK -->
<section class="postcard postcard--back" aria-label="Postcard back">
  <div class="abs about-panel"></div>
  <div class="abs rates-panel"></div>

  <svg class="abs back-band" width="711" height="508" viewBox="0 0 711 508">
    <defs>
      <linearGradient id="houseTones" x1="0" y1="0" x2="0" y2="1">
        <stop offset="0" stop-color="#7fb1e3"/>
        <stop offset=".45" stop-color="#b9a88c"/>
        <stop offset=".75" stop-color="#6f8f4a"/>
        <stop offset="1" stop-color="#4e7f2a"/>
      </linearGradient>
      <linearGradient id="modernTones" x1="0" y1="0" x2="0" y2="1">
        <stop offset="0" stop-color="#8fc1ec"/>
        <stop offset=".5" stop-color="#e7e7ea"/>
        <stop offset=".75" stop-color="#7a6a5c"/>
        <stop offset="1" stop-color="#9aa4a8"/>
      </linearGradient>
      <linearGradient id="bandBlue" x1="0" y1="0" x2="1" y2="0">
        <stop offset="0" stop-color="#2a7cb7"/>
        <stop offset="1" stop-color="#1d6499"/>
      </linearGradient>
    </defs>
    <rect x="0" y="0" width="300" height="0" fill="none"/>
    <path d="M0 430 H372 Q402 470 427 508 H0 Z" fill="url(#bandBlue)"/>
    <path d="M335 330 Q348 420 427 508" fill="none" stroke="var(--navy)" stroke-width="4"/>
    <circle cx="329" cy="288" r="35" fill="var(--navy)"/>
    <circle cx="335" cy="329" r="20" fill="#1d6499"/>
    <circle cx="317" cy="73" r="102" fill="var(--navy)"/>
    <circle cx="319" cy="70" r="95" fill="url(#houseTones)" role="img" aria-label="Photo of a suburban house with garden"/>
    <circle cx="318" cy="178" r="85" fill="var(--navy)"/>
    <circle cx="318" cy="178" r="77" fill="url(#modernTones)" role="img" aria-label="Photo of a modern white home with garage"/>
  </svg>

  <div class="abs about-title">ABOUT US</div>
  <p class="abs about-copy">Veltor Home Fund, a mortgage company based out of Brenford, PA, is led by an executive management team with more than 15 years of experience in the financial industry. We are dedicated to finding the best solution for each borrower. A quickly expanding, privately owned business, Veltor Home Fund works with multiple banks and therefore can find you the right loan product to help you achieve your financial goals.</p>
  <p class="abs rates-copy">Since you're going to be<br>talking about RATES,<br><span class="accent">You will need the ftollowing<br>information as well:</span></p>

  <ul class="abs disclosures">
    <li><svg width="14" height="10" viewBox="0 0 14 10" fill="none" stroke="var(--navy)" stroke-width="1.4"><path d="M1 5 H12 M8 1 L12 5 L8 9"/></svg><span>Amount of the represented loan.</span></li>
    <li><svg width="14" height="10" viewBox="0 0 14 10" fill="none" stroke="var(--navy)" stroke-width="1.4"><path d="M1 5 H12 M8 1 L12 5 L8 9"/></svg><span>Repayment term in years of the represented&nbsp; loan.</span></li>
    <li><svg width="14" height="10" viewBox="0 0 14 10" fill="none" stroke="var(--navy)" stroke-width="1.4"><path d="M1 5 H12 M8 1 L12 5 L8 9"/></svg><span>Prepayment terms.</span></li>
    <li><svg width="14" height="10" viewBox="0 0 14 10" fill="none" stroke="var(--navy)" stroke-width="1.4"><path d="M1 5 H12 M8 1 L12 5 L8 9"/></svg><span>If the advertised rate may increase, the ad must&nbsp; state:<br>"Advertised rate may increase"</span></li>
    <li><svg width="14" height="10" viewBox="0 0 14 10" fill="none" stroke="var(--navy)" stroke-width="1.4"><path d="M1 5 H12 M8 1 L12 5 L8 9"/></svg><span>Statement: "Restrictions may apply. Programs<br>not available in all areas."</span></li>
  </ul>

  <div class="abs lo-photo back-lo-photo" role="img" aria-label="Loan officer portrait"></div>
  <div class="abs back-lo-name">DELVIN OKAFOR</div>
  <div class="abs back-lo-role">MANAGER</div>
  <div class="abs back-lo-mail">
    <svg width="10" height="8" viewBox="0 0 10 8" fill="none" stroke="#9fd0f2" stroke-width="1"><rect x=".5" y=".5" width="9" height="7"/><path d="M.5 .5 L5 4.5 L9.5 .5"/></svg>
    dokafor@veltorhomefund.com
  </div>
  <div class="abs back-phone">
    <svg width="13" height="12" viewBox="0 0 12 11" fill="#9fd0f2"><path d="M1 3 Q6 -1 11 3 L9 5 L8 3 H4 L3 5 Z M3 6 H9 L10 10 H2 Z"/></svg>
    555.294.8163
  </div>
  <div class="abs back-addr">
    <svg width="10" height="12" viewBox="0 0 12 13" fill="#9fd0f2"><path d="M6 0 A5 5 0 0 1 11 5 C11 8 6 13 6 13 C6 13 1 8 1 5 A5 5 0 0 1 6 0 Z"/></svg>
    <span>48 Harlow Commerce Drive<br>Suite 210,Brenford, PA 19077</span>
  </div>

  <div class="abs stamp" aria-label="Stamp area"></div>
  <div class="abs address-line" style="top:258px"></div>
  <div class="abs address-line" style="top:290px"></div>
  <div class="abs address-line" style="top:322px"></div>
  <div class="abs address-line" style="top:354px"></div>

  <div class="abs back-brand">veltor<span class="brand__mark"></span></div>
  <div class="abs back-url">www.veltorhomefund.com</div>
</section>

</body>
</html>
```